Sleek and elegant promotional banner/sign for The Belvane Law Firm

We need a design for promotional items like banners, signs, print ads, etc. that includes our firm name - "The Belvane Law Firm" - and what we do. We advise businesses and individuals on legal matters; we represent individuals and businesses in litigation and transactions; we select and create business entities; we solve legal problems for individuals and businesses, etc. PLEASE DO NOT SIMPLY REPEAT THE PREVIOUS SENTENCE ON THE DESIGN. Please create a tag-line or brief description from ours. We need something that describes what we do in concise and creative manner while communicating trust and confidence. The banner must also include our basic contact information: 818.452-7196 (telephone) and belvanelaw.example (website). You may use one or more of the attached images, but needn't use any with the right design. The design should be sleek and modern.

Target Market(s)

wealthy individuals and small business owners, entrepreneurs

Industry/Entity Type

Lawyer

Font styles to use
Sans Serif

Colors
33a6d7
0556a4
33b8a4

Requirements
Must have
• Firm name, contact information, BRIEF description of our services, sleek and elegant.
• Also, the design must be horizontal - not vertical.
Nice to have
• I'd like to use one of the images
Should not have
• Cliches

```html
<!DOCTYPE html>
<html lang="en">
<head>
<meta charset="utf-8">
<title>The Belvane Law Firm – Banner</title>
<link rel="stylesheet" href="https://fonts.googleapis.com/css2?family=Jost:wght@300;400;500;600&display=swap">
<style>
  :root {
    --navy: #0556a4;
    --navy-deep: #0a4c9c;
    --sky: #33a6d7;
    --sky-deep: #1f7fb8;
    --teal: #33b8a4;
    --teal-soft: #3dbfa8;
    --teal-deep: #2fae99;
    --white: #ffffff;
    --line: rgba(255,255,255,0.85);
  }
  * { box-sizing: border-box; margin: 0; padding: 0; }
  html, body { width: 1200px; height: 771px; overflow: hidden; background: #f2f2f2; }
  body { font-family: "Jost", "Futura", sans-serif; color: var(--white); }

  .banner { position: relative; width: 1200px; height: 771px; display: flex; flex-direction: column; }

  .masthead {
    height: 200px; background: var(--navy-deep);
    display: flex; align-items: center; padding-left: 108px;
  }
  .firm-name {
    display: flex; align-items: center; gap: 28px;
    font-weight: 400; font-size: 58px; letter-spacing: 0.28em; text-transform: uppercase; line-height: 1;
  }
  .firm-mark { width: 22px; height: 22px; background: var(--white); flex: none; }

  .hero { position: relative; height: 312px; background: var(--sky); overflow: hidden; }
  .hero-image {
    position: absolute; inset: 0 0 0 300px;
    background: radial-gradient(ellipse at 35% 55%, #3aa7dc 0%, #2e93cc 45%, #2579b4 100%);
  }
  .hero-fade { position: absolute; inset: 0; background: linear-gradient(90deg, var(--sky) 0%, var(--sky) 28%, rgba(51,166,215,0) 55%); }
  .tagline {
    position: relative; padding: 36px 0 0 164px;
    font-weight: 500; font-size: 56px; line-height: 83px; letter-spacing: 0.005em;
  }

  .services { height: 142px; display: flex; }
  .service { display: flex; align-items: center; height: 100%; }
  .service--business-law { width: 402px; background: var(--teal-deep); padding-left: 80px; }
  .service--litigation { width: 376px; background: var(--teal-soft); padding-left: 18px; }
  .service--estate { width: 422px; background: var(--teal); padding-left: 20px; }
  .service-icon { width: 76px; height: 76px; flex: none; }
  .service-divider { width: 2px; height: 76px; background: var(--line); margin: 0 22px 0 24px; flex: none; }
  .service-label { font-size: 38px; line-height: 42px; text-transform: uppercase; }
  .service-label .light { display: block; font-weight: 300; }
  .service-label .bold { display: block; font-weight: 600; }

  .contact {
    height: 117px; background: var(--navy);
    display: flex; align-items: center; justify-content: space-between; padding: 0 71px 0 75px;
  }
  .contact-item { display: flex; align-items: center; gap: 20px; }
  .contact-phone { font-size: 54px; font-weight: 500; letter-spacing: 0.01em; }
  .contact-web { font-size: 40px; font-weight: 500; gap: 12px; }
</style>
</head>
<body>
<main class="banner">
  <header class="masthead">
    <div class="firm-name"><span class="firm-mark"></span>Belvane Law</div>
  </header>

  <section class="hero">
    <div class="hero-image" role="img" aria-label="Photograph of interlocking blue jigsaw puzzle pieces arranged in a spiral"></div>
    <div class="hero-fade"></div>
    <h1 class="tagline">we solve<br>the most puzzling<br>legal problems</h1>
  </section>

  <section class="services">
    <div class="service service--business-law">
      <svg class="service-icon" viewBox="0 0 76 76" fill="none" stroke="#fff" stroke-width="2.5" stroke-linejoin="round">
        <rect x="28" y="6" width="16" height="30" rx="2" transform="rotate(45 36 21)"/>
        <line x1="30" y1="30" x2="6" y2="54"/>
        <line x1="34" y1="34" x2="10" y2="58"/>
        <rect x="38" y="56" width="22" height="8"/>
        <rect x="32" y="64" width="34" height="8"/>
      </svg>
      <span class="service-divider"></span>
      <p class="service-label"><span class="light">Business</span><span class="bold">Law</span></p>
    </div>

    <div class="service service--litigation">
      <svg class="service-icon" viewBox="0 0 76 76" fill="none" stroke="#fff" stroke-width="2.5" stroke-linejoin="round">
        <line x1="38" y1="8" x2="38" y2="64"/>
        <line x1="12" y1="18" x2="64" y2="14"/>
        <path d="M12 18 L4 40 M12 18 L20 40 M4 40 Q12 50 20 40 Z"/>
        <path d="M64 14 L56 36 M64 14 L72 36 M56 36 Q64 46 72 36 Z"/>
        <rect x="26" y="64" width="24" height="6"/>
        <circle cx="38" cy="8" r="3"/>
      </svg>
      <span class="service-divider"></span>
      <p class="service-label"><span class="light">Business</span><span class="bold">Litigation</span></p>
    </div>

    <div class="service service--estate">
      <svg class="service-icon" viewBox="0 0 76 76" fill="none" stroke="#fff" stroke-width="2.5">
        <rect x="6" y="6" width="64" height="64"/>
        <line x1="6" y1="38" x2="40" y2="38"/>
        <line x1="40" y1="6" x2="40" y2="52"/>
        <line x1="40" y1="52" x2="70" y2="52"/>
        <line x1="24" y1="38" x2="24" y2="70"/>
        <circle cx="56" cy="22" r="6"/>
        <rect x="12" y="46" width="8" height="18"/>
      </svg>
      <span class="service-divider"></span>
      <p class="service-label"><span class="light">Estate</span><span class="bold">Planning</span></p>
    </div>
  </section>

  <footer class="contact">
    <div class="contact-item contact-phone">
      <svg width="50" height="50" viewBox="0 0 50 50" fill="none" stroke="#fff" stroke-width="2.5">
        <circle cx="25" cy="25" r="22.5"/>
        <path d="M17 13 l5 0 l2 7 l-3 3 q3 6 9 9 l3 -3 l7 2 l0 5 q-1 3 -5 3 q-12 -2 -20 -14 q-3 -6 -1 -10 z" stroke-linejoin="round"/>
      </svg>
      <span>818.452-7196</span>
    </div>
    <div class="contact-item contact-web">
      <svg width="36" height="36" viewBox="0 0 36 36" fill="none" stroke="#fff" stroke-width="2.2">
        <circle cx="18" cy="18" r="15"/>
        <ellipse cx="18" cy="18" rx="7" ry="15"/>
        <line x1="3" y1="18" x2="33" y2="18"/>
        <path d="M6 10 H30 M6 26 H30"/>
      </svg>
      <span>belvanelaw.example</span>
    </div>
  </footer>
</main>
</body>
</html>
```